Morvel

We are openıng one huntıng showroom in Riyadh? Saudi Arabia. Company name is "MORVEL".
Our logo designed and we need Business Card Design now.
I attached MORVEL logo below.
Front side will English and back side will be Arabic

```html
<!DOCTYPE html>
<html lang="en">
<head>
<meta charset="utf-8">
<title>Morvel Business Card</title>
<link rel="stylesheet" href="https://fonts.googleapis.com/css2?family=Lato:wght@400;700&family=Exo+2:wght@600&display=swap">
<style>
  :root {
    --bg: #d9d9d9;
    --card: #ffffff;
    --band: #7a9e3d;
    --stripe: #0a7a3b;
    --brand: #0a7a3b;
    --ink: #2a2a2a;
  }
  html, body {
    margin: 0;
    width: 1200px;
    height: 802px;
    overflow: hidden;
    background: var(--bg);
  }
  .card {
    position: absolute;
    left: 50px;
    top: 72px;
    width: 1100px;
    height: 658px;
    background: var(--card);
    box-shadow: 0 4px 14px rgba(0,0,0,.18);
    font-family: "Lato", sans-serif;
    color: var(--ink);
  }
  .side-band {
    position: absolute;
    left: 0; top: 0;
    width: 105px; height: 100%;
    background: var(--band);
  }
  .side-stripe {
    position: absolute;
    left: 105px; top: 0;
    width: 10px; height: 100%;
    background: var(--stripe);
  }
  .brand-name {
    position: absolute;
    right: 75px;
    top: 62px;
    margin: 0;
    font-family: "Lato", sans-serif;
    font-weight: 700;
    font-size: 86px;
    letter-spacing: 1px;
    color: var(--brand);
    line-height: 1;
  }
  .person {
    position: absolute;
    left: 176px;
    top: 250px;
  }
  .person-name {
    margin: 0;
    font-family: "Exo 2", sans-serif;
    font-weight: 600;
    font-size: 33px;
    color: var(--brand);
    line-height: 1.05;
  }
  .person-title {
    margin: 0;
    font-size: 30px;
    line-height: 1.15;
  }
  .contacts {
    position: absolute;
    left: 176px;
    top: 340px;
    margin: 0;
    padding: 0;
    list-style: none;
    font-size: 30px;
  }
  .contacts li {
    display: flex;
    align-items: center;
    height: 36.7px;
  }
  .contacts svg {
    width: 24px;
    height: 24px;
    margin-right: 14px;
    fill: var(--brand);
    flex: none;
  }
  .address {
    position: absolute;
    left: 176px;
    top: 520px;
    margin: 0;
    font-style: normal;
    font-size: 30px;
    line-height: 39px;
  }
</style>
</head>
<body>
  <div class="card">
    <div class="side-band"></div>
    <div class="side-stripe"></div>

    <p class="brand-name">MORVEL</p>

    <div class="person">
      <p class="person-name">Faisal Omar K ALHARBI</p>
      <p class="person-title">Executive Manager</p>
    </div>

    <ul class="contacts">
      <li>
        <svg viewBox="0 0 24 24" aria-hidden="true"><path d="M7 1h10a2 2 0 0 1 2 2v18a2 2 0 0 1-2 2H7a2 2 0 0 1-2-2V3a2 2 0 0 1 2-2zm0 3v14h10V4zm5 15.5a1.2 1.2 0 1 0 0 2.4 1.2 1.2 0 0 0 0-2.4z"/></svg>
        +966 500 318 742
      </li>
      <li>
        <svg viewBox="0 0 24 24" aria-hidden="true"><path d="M2 8c0-3 5-5 10-5s10 2 10 5v2h-5V8c-1-1-3-1.5-5-1.5S8 7 7 8v2H2zm4 4h12l3 9H3zm6 2a3 3 0 1 0 0 6 3 3 0 0 0 0-6z"/></svg>
        011 238 46 90
      </li>
      <li>
        <svg viewBox="0 0 24 24" aria-hidden="true"><path d="M6 2h12v6H6zM3 9h18a1 1 0 0 1 1 1v8h-4v4H6v-4H2v-8a1 1 0 0 1 1-1zm5 7v4h8v-4z"/></svg>
        0112384691
      </li>
      <li>
        <svg viewBox="0 0 24 24" aria-hidden="true"><path d="M2 5h20v14H2zm2 2v1l8 6 8-6V7zm0 3.5V17h16v-6.5l-8 6z"/></svg>
        morvel.ksa@mailbox.sa
      </li>
      <li>
        <svg viewBox="0 0 24 24" aria-hidden="true"><path d="M12 1a11 11 0 1 0 0 22 11 11 0 0 0 0-22zm-2 4c2 0 3 1 2 3s-3 1-3 3 3 1 3 4-2 4-3 4c0-2-1-3-2-4s-2-3-1-5 2-2 4-5zm6 2c2 1 3 3 3 5s-1 3-2 3-2-2-1-4-1-3 0-4z"/></svg>
        www.morvel.com.sa
      </li>
    </ul>

    <address class="address">
      Nakheel Street Al Wadi<br>
      P.O. Box 4412 - 13321, Kingdom of Saudi Arabia
    </address>
  </div>
</body>
</html>
```